New Website for consulting company

We need a completely new design for our company web site: www.morvane-partners.ch (please do not use it as a reference. We want something completely different.)
We are a consulting company and therefore our team is our key ressource together with our skills.
This site will be german in the first place. It will be the webmasters job to create it multilingual.
The website should be rather eccentric but still informative.
For colors and logo please refer to attached Logodefinition.pdf. The colored horizontal logo should be somehow used for the website but doesn't need to be extremely prominent. You can choose every color for the design but the logo must be somehow embedded in original colors and the green should be integrated for the site.
Please keep in mind that it should also work for mobile devices so the webmaster will have to create a responsive website out of the submitted design.
The main Page should be a one pager with different layout blocks directly accessible via top sticky menubar.:
- AKTEURE (team), gallery, people centric with images of member and expandable description box, plus skills abstract list (name & description). See attached mockups to support the explaining (do not take it as a reference).
- ÜBER UNS (mission), Description of companies vision, mission, competences etc.
- ... according to the menu bar
We would like to have at least 3 different block layouts to fill with content for the one pager site:
1. Team is the most important and the least generic one
2. Big picture less text
3. Multiple smaller pictures multiple text blocks
4. Hardly any picture text centric
The page should communicate competence in what we are doing, quality and not least youth and freshness.
See Attachements:
- Logodefinition.pdf: Logo definition containing definition of color of the logo.
- mockup_Website_mock1.png: These should give you an impression of how it is meant to have layouted blocks

```html
<!DOCTYPE html>
<html lang="de">
<head>
<meta charset="utf-8">
<title>Morvane Partners – Startseite</title>
<link href="https://fonts.googleapis.com/css2?family=Open+Sans:wght@300;400;600;700;800&display=swap" rel="stylesheet">
<style>
  :root {
    --green: #5cb531;
    --green-dark: #4aa326;
    --blue: #1a56e8;
    --ink: #111111;
    --text: #222222;
    --white: #ffffff;
  }
  * { box-sizing: border-box; margin: 0; padding: 0; }
  html, body { width: 1200px; height: 3704px; overflow: hidden; background: var(--white); }
  body { position: relative; font-family: "Open Sans", Arial, sans-serif; color: var(--text); }
  .abs { position: absolute; }

  /* Header */
  .brand { left: 0; top: 25px; display: flex; align-items: center; gap: 18px; }
  .brand-mark { width: 123px; height: 123px; background: var(--green); }
  .brand-name { font-weight: 600; color: var(--green); font-size: 40px; line-height: 1; }
  .main-nav { left: 889px; top: 74px; display: flex; gap: 26px; }
  .main-nav a { font-size: 20px; font-weight: 300; color: var(--ink); text-decoration: none; letter-spacing: -0.5px; }

  /* Topic tiles */
  .tile-photo { width: 408px; height: 410px; }
  .tile-label { font-weight: 700; font-size: 43px; color: var(--ink); letter-spacing: 0.5px; line-height: 1; }
  .tile-square { width: 40px; height: 40px; background: var(--green); }

  .photo-track { background: linear-gradient(180deg, #9fb6a4 0%, #b98e7c 45%, #c47a66 100%); }
  .photo-rowing { background: linear-gradient(160deg, #3b4e7a 0%, #26324f 45%, #d9dde2 70%, #8f99a5 100%); }
  .photo-handshake { background: linear-gradient(180deg, #f0f0ee 0%, #d8dcd6 40%, #3a3a3c 100%); }
  .photo-network { background: radial-gradient(circle at 35% 35%, #e7e9f3 0%, #9fb3cf 45%, #56607a 100%); }
  .photo-business { background: linear-gradient(160deg, #eceff2 0%, #9aa3ad 45%, #3a4452 100%); }

  .claim { left: 667px; top: 1390px; width: 500px; }
  .claim h2 { color: var(--green); font-weight: 700; font-size: 42px; line-height: 1.2; letter-spacing: 0.5px; }
  .claim p { margin-top: 30px; font-size: 23px; line-height: 1.15; color: var(--ink); }

  /* Team */
  .team { left: 44px; top: 1938px; width: 1109px; height: 803px; border: 12px solid var(--blue); }
  .team h2 { position: absolute; left: 82px; top: 78px; font-size: 44px; font-weight: 700; color: var(--ink); }
  .team-intro { position: absolute; left: 53px; top: 150px; width: 380px; font-size: 19.5px; line-height: 31px; color: var(--ink); }
  .team-more { position: absolute; left: 53px; top: 615px; width: 222px; height: 55px; border: 5px solid var(--blue);
    color: var(--blue); font-weight: 700; font-size: 22px; display: flex; align-items: center; justify-content: center; }
  .member { position: absolute; width: 139px; text-align: center; }
  .member-photo { width: 139px; height: 166px; background: linear-gradient(180deg, #f2f2f2 0%, #dcdfe3 55%, #6d7a8c 100%); }
  .member-name { margin-top: 20px; font-size: 15px; font-weight: 700; color: var(--ink); line-height: 1; }
  .member-role { margin-top: 6px; font-size: 12px; color: var(--ink); line-height: 1; }

  /* Video band */
  .video { left: 0; top: 2827px; width: 1200px; height: 531px;
    background: linear-gradient(100deg, #8d8a86 0%, #b3b5b8 35%, #d5d8dc 60%, #9a9590 100%); }
  .play { left: 440px; top: 3057px; width: 325px; height: 74px; border: 4px solid var(--white);
    display: flex; align-items: center; justify-content: center; gap: 26px;
    color: var(--white); font-weight: 600; font-size: 28px; }

  /* Footer */
  .site-footer { left: 0; top: 3427px; width: 1200px; height: 277px; background: var(--green); }
  .footer-links { position: absolute; top: 58px; list-style: none; }
  .footer-links li { font-size: 19px; font-weight: 300; color: var(--white); line-height: 33px; letter-spacing: -0.4px; }
  .social { position: absolute; top: 62px; width: 64px; height: 64px; background: var(--white); }
</style>
</head>
<body>

<header>
  <div class="abs brand">
    <span class="brand-mark"></span>
    <span class="brand-name">Morvane Partners</span>
  </div>
  <nav class="abs main-nav">
    <a href="#">HOME</a><a href="#">JOBS</a><a href="#">KONTAKT</a>
  </nav>
</header>

<main>
  <div class="abs tile-photo photo-track" style="left:136px;top:185px" role="img" aria-label="Geschäftsleute in Startposition auf einer Laufbahn"></div>
  <div class="abs tile-label" style="left:168px;top:578px">KOMPETENZEN</div>
  <div class="abs tile-square" style="left:114px;top:627px"></div>

  <div class="abs tile-photo photo-rowing" style="left:657px;top:274px" role="img" aria-label="Ruderteam im Gleichtakt auf dem Wasser"></div>
  <div class="abs tile-label" style="left:905px;top:668px">TEAM</div>
  <div class="abs tile-square" style="left:1052px;top:716px"></div>

  <div class="abs tile-photo photo-handshake" style="left:136px;top:765px" role="img" aria-label="Zwei Geschäftsfrauen beim Händedruck"></div>
  <div class="abs tile-label" style="left:168px;top:1158px">KUNDEN</div>
  <div class="abs tile-square" style="left:114px;top:1205px"></div>

  <div class="abs tile-photo photo-network" style="left:657px;top:830px" role="img" aria-label="Hand berührt ein digitales Netzwerk aus Personensymbolen"></div>
  <div class="abs tile-label" style="left:786px;top:1226px">NETZWERK</div>
  <div class="abs tile-square" style="left:1052px;top:1271px"></div>

  <div class="abs tile-photo photo-business" style="left:136px;top:1348px" role="img" aria-label="Zwei Berater besprechen sich am Tablet"></div>
  <div class="abs tile-label" style="left:168px;top:1741px">UNTERNEHMEN</div>
  <div class="abs tile-square" style="left:114px;top:1788px"></div>

  <section class="abs claim">
    <h2>EINE<br>ZUSAMMENARBEI<br>T, DIE FRÜCHTE<br>TRÄGT.</h2>
    <p>Die Herausforderungen unserer Kunden sind geprägt durch stetig wachsende Qualitätsansprüche, durch immer schnellere Veränderungszyklen</p>
  </section>

  <section class="abs team">
    <h2>AKTEURE</h2>
    <p class="team-intro">Lorem ipsum dolor sit amet, consectetur adipiscing elit. Vivamus faucibus blandit libero, sed mattis leo faucibus nec. Aliquam mattis porta sapien a bibendum. Aenean interdum ac risus a dapibus. Ut at aliquam diam. Pellentesque est risus, molestie vel elit et, euismod aliquet ipsum. Sed at fringilla urna. Nulla facilisi. Vivamus aliquam ligula odio, sed finibus tortor pulvinar in. Sed malesuada vehicula ipsum, at sagittis ligula facilisis vitae. Aenean condimentum feugiat sem, sit amet rutrum ligula. Duis blandit lacus eget ipsum vehicula pulvinar.</p>
    <div class="team-more">MORE</div>

    <div class="member" style="left:514px;top:30px"><div class="member-photo" role="img" aria-label="Porträt Teammitglied"></div><div class="member-name">JONAS MEIER</div><div class="member-role">Project Manager</div></div>
    <div class="member" style="left:690px;top:30px"><div class="member-photo" role="img" aria-label="Porträt Teammitglied"></div><div class="member-name">JONAS MEIER</div><div class="member-role">Project Manager</div></div>
    <div class="member" style="left:865px;top:30px"><div class="member-photo" role="img" aria-label="Porträt Teammitglied"></div><div class="member-name">JONAS MEIER</div><div class="member-role">Project Manager</div></div>

    <div class="member" style="left:514px;top:282px"><div class="member-photo" role="img" aria-label="Porträt Teammitglied"></div><div class="member-name">JONAS MEIER</div><div class="member-role">Project Manager</div></div>
    <div class="member" style="left:690px;top:282px"><div class="member-photo" role="img" aria-label="Porträt Teammitglied"></div><div class="member-name">JONAS MEIER</div><div class="member-role">Project Manager</div></div>
    <div class="member" style="left:865px;top:282px"><div class="member-photo" role="img" aria-label="Porträt Teammitglied"></div><div class="member-name">JONAS MEIER</div><div class="member-role">Project Manager</div></div>

    <div class="member" style="left:514px;top:531px"><div class="member-photo" role="img" aria-label="Porträt Teammitglied"></div><div class="member-name">JONAS MEIER</div><div class="member-role">Project Manager</div></div>
    <div class="member" style="left:690px;top:531px"><div class="member-photo" role="img" aria-label="Porträt Teammitglied"></div><div class="member-name">JONAS MEIER</div><div class="member-role">Project Manager</div></div>
    <div class="member" style="left:865px;top:531px"><div class="member-photo" role="img" aria-label="Porträt Teammitglied"></div><div class="member-name">JONAS MEIER</div><div class="member-role">Project Manager</div></div>
  </section>

  <section class="abs video" role="img" aria-label="Team in einer Besprechung am Konferenztisch"></section>
  <div class="abs play">
    <svg width="18" height="20" viewBox="0 0 18 20" aria-hidden="true"><polygon points="0,0 18,10 0,20" fill="#ffffff"/></svg>
    <span>PLAY VIDEO</span>
  </div>
</main>

<footer class="abs site-footer">
  <ul class="footer-links" style="left:74px">
    <li>HOME</li><li>JOBS</li><li>KONTAKT</li>
  </ul>
  <ul class="footer-links" style="left:301px">
    <li>Kompetenzen</li><li>Team</li><li>Kunden</li><li>Netzwerk</li><li>Unternehmen</li>
  </ul>
  <span class="social" style="left:896px"></span>
  <span class="social" style="left:980px"></span>
  <span class="social" style="left:1064px"></span>
</footer>

</body>
</html>
```